HTML Email template look and feel

Hi, we have been sending out various emails to our clients and they have been a mix of anything from plain text to some html emails that were done for us, i am looking to get a nice design and layout for our HTML emails to keep them looking professional and consistent. What I am looking for is an html email template that has a nice edgy but professional look and feel. Ie header and table styling i suppose. Most of the data we send is either in a 2 or 4 column table layout as such.
Table A
Firm A 6
Firm B 124
Firm C 32435
Table B
Firm A 6 Firm D 4546
Firm B 124 Firm E 3545
Firm C 32435 Firm F 44
For some background our website is http://www.quellmarkets.example/
and our logo is on there, and i have attached one of the html emails we are currently sending.
Reason: Just wanted to see what comes in over the weekend before we decide

```html
<!DOCTYPE html>
<html lang="en">
<head>
<meta charset="utf-8">
<title>Quell Markets Newsletter</title>
<link rel="stylesheet" href="https://fonts.googleapis.com/css2?family=Noto+Sans:wght@400;700&family=Arimo:wght@400&display=swap">
<style>
  :root {
    --blue: #1a9ad6;
    --ink: #111;
    --text: #555;
    --muted: #888;
    --rule: #d3d3d3;
    --frame: #8a8a8a;
    --cell-line: #dcdcdc;
    --photo: #a8a8a8;
    --logo-grey: #555;
  }
  * { box-sizing: border-box; margin: 0; padding: 0; }
  html, body { width: 1000px; height: 1200px; overflow: hidden; background: #fff; }
  body { position: relative; font-family: "Noto Sans", sans-serif; color: var(--ink); }
  .mail { position: absolute; left: 185px; top: 35px; width: 631px; height: 1007px; border: 1px solid var(--frame); }
  .abs { position: absolute; }

  .toolbar { left: 15px; top: 8px; width: 600px; font-family: "Arimo", sans-serif; font-size: 11px; color: var(--blue); }
  .toolbar a { color: var(--blue); text-decoration: none; display: flex; align-items: center; gap: 6px; position: absolute; top: 0; white-space: nowrap; }
  .dash { left: 14px; width: 602px; border-top: 2px dashed #ddd; }
  .rule { left: 14px; width: 602px; border-top: 1px solid var(--rule); }
  .rule::after { content: ""; position: absolute; left: 40px; right: 40px; top: 0; height: 10px; background: radial-gradient(ellipse at top, rgba(0,0,0,.08), transparent 70%); }

  .brand { left: 14px; top: 62px; display: flex; align-items: center; gap: 12px; font-size: 38px; letter-spacing: 1px; color: var(--logo-grey); line-height: 1; }
  .brand .mark { width: 22px; height: 22px; background: var(--blue); }
  .brand small { display: block; font-size: 11px; letter-spacing: 9px; margin-top: 4px; }

  .stat { left: 330px; width: 156px; top: 66px; text-align: right; color: var(--blue); font-size: 24px; line-height: 1; white-space: nowrap; }
  .stat span { display: block; font-size: 15px; margin-top: 1px; }
  .stat-div { left: 506px; top: 69px; height: 34px; border-left: 1px solid #bbb; }
  .date { right: 13px; top: 64px; display: flex; color: var(--blue); align-items: center; }
  .date .day { font-size: 42px; line-height: 1; }
  .date .my { font-size: 18px; line-height: 1; margin-left: 2px; }

  .news { top: 182px; width: 191px; }
  .news .photo { height: 101px; background: linear-gradient(var(--photo), #a0a0a0); border-bottom: 1px solid #888; }
  .news h2 { font-weight: 400; font-size: 17px; margin-top: 9px; white-space: nowrap; }
  .news p { font-size: 11px; line-height: 14px; color: var(--text); margin: 9px 0 0 2px; letter-spacing: -0.1px; }

  .sec-title { left: 14px; display: flex; align-items: center; gap: 8px; font-size: 12px; font-weight: 700; white-space: nowrap; }
  .badge { width: 27px; height: 27px; border-radius: 50%; background: var(--blue); color: #fff; font-size: 15px; display: flex; align-items: center; justify-content: center; }
  .chart-ico { margin-left: 6px; }

  table { border-collapse: collapse; font-family: "Arimo", sans-serif; position: absolute; left: 14px; width: 602px; table-layout: fixed; }
  th, td { border: 1px solid var(--cell-line); text-align: center; }
  th { height: 31px; font-weight: 400; font-size: 14px; color: #222; background: repeating-linear-gradient(135deg, #f5f5f5 0 2px, #ececec 2px 3px); }
  td { height: 26px; font-size: 12px; color: var(--muted); }
  .sector td { border-left: none; border-right: none; }
  .sector td.split { border-right: 1px solid var(--cell-line); }
  .sector td:first-child { border-left: 1px solid var(--cell-line); }
  .sector td:last-child { border-right: 1px solid var(--cell-line); }

  .footer { left: 14px; top: 931px; font-family: "Arimo", sans-serif; font-size: 12px; line-height: 18px; color: #222; white-space: nowrap; }
  .footer .social { display: flex; gap: 14px; margin-top: 3px; align-items: center; }
  .footer .social span { display: flex; align-items: center; gap: 7px; }
  .sq { width: 16px; height: 16px; border-radius: 2px; display: inline-block; }
  .footer-brand { right: 14px; top: 934px; display: flex; align-items: center; gap: 10px; font-size: 30px; color: #7a7a7a; line-height: 1; }
  .footer-brand .mark { width: 18px; height: 18px; background: #7a7a7a; }
  .footer-brand small { display: block; font-size: 9px; letter-spacing: 7px; margin-top: 3px; }
</style>
</head>
<body>
<div class="mail">
  <nav class="toolbar abs">
    <a style="left:40px"><svg width="14" height="13"><circle cx="7" cy="4" r="3.5" fill="#1a7fb8"/><path d="M0 13c0-5 14-5 14 0z" fill="#1a7fb8"/></svg>Forward to a friend</a>
    <a style="left:195px"><svg width="16" height="14"><rect x="0" y="0" width="16" height="11" rx="1" fill="#1a7fb8"/><rect x="2" y="2" width="12" height="7" fill="#9fd3ef"/><rect x="5" y="12" width="6" height="2" fill="#1a7fb8"/></svg>Online Version</a>
    <a style="left:338px"><svg width="10" height="15"><rect width="10" height="15" rx="2" fill="#1a7fb8"/><rect x="2" y="2" width="6" height="9" fill="#9fd3ef"/></svg>Mobile Version</a>
    <a style="left:480px"><svg width="16" height="16" viewBox="0 0 16 16"><circle cx="8" cy="8" r="6" fill="none" stroke="#1a7fb8" stroke-width="4" stroke-dasharray="3 2"/><circle cx="8" cy="8" r="4" fill="#1a7fb8"/><circle cx="8" cy="8" r="2" fill="#fff"/></svg>Unsubscribe</a>
  </nav>
  <div class="dash abs" style="top:37px"></div>

  <div class="brand abs"><span class="mark"></span><div>QUELL<small>MARKETS</small></div></div>
  <div class="stat abs">27,490,544<span>Shares Executed*</span></div>
  <div class="stat-div abs"></div>
  <div class="date abs"><span class="day">01</span><span class="my">Dec<br>2011</span></div>
  <div class="rule abs" style="top:142px"></div>

  <article class="news abs" style="left:14px"><div class="photo" role="img" aria-label="News photo placeholder"></div><h2>Quell Recent News 1</h2><p>Aenean leo ligula, porttitor eu, consequat vitae, eleifend ac, enim. Aliquam lorem ante, dapibus in, viverra quis, feugiat a, tellus. Nam</p></article>
  <article class="news abs" style="left:220px"><div class="photo" role="img" aria-label="News photo placeholder"></div><h2>Quell Recent News 2</h2><p>Aenean leo ligula, porttitor eu, consequat vitae, eleifend ac, enim. Aliquam lorem ante, dapibus in, viverra quis, feugiat a, tellus. Nam</p></article>
  <article class="news abs" style="left:425px"><div class="photo" role="img" aria-label="News photo placeholder"></div><h2>Quell Recent News 3</h2><p>Aenean leo ligula, porttitor eu, consequat vitae, eleifend ac, enim. Aliquam lorem ante, dapibus in, viverra quis, feugiat a, tellus. Nam</p></article>

  <div class="dash abs" style="top:407px"></div>

  <div class="sec-title abs" style="top:424px"><span class="badge">10</span>Top 10 Symbols As % Of Volume
    <svg class="chart-ico" width="29" height="25"><rect width="29" height="25" fill="#bdbdbd" stroke="#999"/><g fill="#666"><rect x="5" y="13" width="2" height="9"/><rect x="9" y="9" width="2" height="13"/><rect x="13" y="6" width="2" height="16"/><rect x="17" y="10" width="2" height="12"/><rect x="21" y="7" width="2" height="15"/></g></svg></div>
  <table style="top:467px">
    <thead><tr><th>Symbol</th><th>%</th><th>Symbol</th><th>%</th></tr></thead>
    <tbody>
      <tr><td>QRLN</td><td>23.84%</td><td>QRLN</td><td>23.84%</td></tr>
      <tr><td>MVTX</td><td>16.71%</td><td>MVTX</td><td>16.71%</td></tr>
      <tr><td>DABR</td><td>14.61%</td><td>DABR</td><td>14.61%</td></tr>
      <tr><td>KOLT</td><td>13.27%</td><td>KOLT</td><td>13.27%</td></tr>
      <tr><td>PENW</td><td>13.27%</td><td>PENW</td><td>13.27%</td></tr>
    </tbody>
  </table>

  <div class="sec-title abs" style="top:642px"><span class="badge">5</span>Top 5 by Sector
    <svg class="chart-ico" width="29" height="25"><rect width="29" height="25" fill="#bdbdbd" stroke="#999"/><g fill="#666"><rect x="5" y="13" width="2" height="9"/><rect x="9" y="9" width="2" height="13"/><rect x="13" y="6" width="2" height="16"/><rect x="17" y="10" width="2" height="12"/><rect x="21" y="7" width="2" height="15"/></g></svg></div>

  <table class="sector" style="top:685px">
    <thead><tr><th colspan="5">Consumer Discretionary</th><th colspan="5">Industrial</th></tr></thead>
    <tbody><tr><td>MVTX</td><td>MVTX</td><td>MVTX</td><td>MVTX</td><td class="split">MVTX</td><td>MVTX</td><td>MVTX</td><td>MVTX</td><td>MVTX</td><td>MVTX</td></tr></tbody>
  </table>
  <table class="sector" style="top:755px">
    <thead><tr><th colspan="5">Consumer Discretionary</th><th colspan="5">Industrial</th></tr></thead>
    <tbody><tr><td>MVTX</td><td>MVTX</td><td>MVTX</td><td>MVTX</td><td class="split">MVTX</td><td>MVTX</td><td>MVTX</td><td>MVTX</td><td>MVTX</td><td>MVTX</td></tr></tbody>
  </table>
  <table class="sector" style="top:825px">
    <thead><tr><th colspan="5">Consumer Discretionary</th><th colspan="5">Industrial</th></tr></thead>
    <tbody><tr><td>MVTX</td><td>MVTX</td><td>MVTX</td><td>MVTX</td><td class="split">MVTX</td><td>MVTX</td><td>MVTX</td><td>MVTX</td><td>MVTX</td><td>MVTX</td></tr></tbody>
  </table>

  <div class="rule abs" style="top:902px"></div>

  <footer class="footer abs">
    <div>Copyright © 2011 Company Name. All Rights Reserved.</div>
    <div>1234 Main Street | City | State 12345 | you@yoursite.com</div>
    <div class="social"><span><i class="sq" style="background:#f08a24"></i>RSS</span><span><i class="sq" style="background:#5bb8e8"></i>Follow Us</span></div>
  </footer>
  <div class="footer-brand abs"><span class="mark"></span><div>QUELL<small>MARKETS</small></div></div>
</div>
</body>
</html>
```